Business cards real estate company

We need a design for a business card. It is a company that specializes in real estate sales. There should be space for a photo of the respective employee as well as the website and telephone number on it. Design should be noble, innovative.

Contact Information for Business Card

Website, Name, Position, Telefonnummer

Requirements
Must have
• Photo, logo

```html
<!DOCTYPE html>
<html lang="en">
<head>
<meta charset="utf-8">
<title>Corvale business cards</title>
<link href="https://fonts.googleapis.com/css2?family=Montserrat:wght@400;500;700&display=swap" rel="stylesheet">
<style>
  :root {
    --backdrop: #4a4a4a;
    --card: #1c1c1c;
    --edge: #6cc04a;
    --brand: #8fd032;
    --text: #f2f2f2;
    --muted: #d6d6d6;
    --photo-dark: #1c1c1c;
    --photo-light: #b9cde6;
  }
  * { box-sizing: border-box; margin: 0; padding: 0; }
  html, body {
    width: 1200px; height: 801px; overflow: hidden;
    background: var(--backdrop);
    font-family: "Montserrat", sans-serif;
  }
  .sheet {
    position: relative; width: 1200px; height: 801px;
    display: flex; align-items: center; justify-content: center; gap: 50px;
  }
  .card {
    position: relative; width: 530px; height: 303px;
    background: var(--card);
    border: 2px solid var(--edge);
    border-radius: 18px;
    overflow: hidden;
  }
  /* front */
  .card-front .portrait {
    position: absolute; top: 0; right: 0; width: 240px; height: 100%;
    background: radial-gradient(ellipse at 70% 55%, var(--photo-light) 0%, #7f93ad 35%, var(--photo-dark) 75%);
  }
  .card-front .edge-tab {
    position: absolute; left: -2px; top: 232px; width: 10px; height: 26px;
    background: var(--brand); border-radius: 0 6px 6px 0;
  }
  .card-front .details {
    position: absolute; left: 34px; top: 34px;
  }
  .brand-name {
    font-weight: 700; color: var(--brand); letter-spacing: 0.5px; line-height: 1;
  }
  .card-front .brand-name { font-size: 46px; }
  .person-name {
    margin-top: 18px; font-size: 20px; font-weight: 700; color: var(--brand);
  }
  .person-role { font-size: 14px; color: var(--muted); margin-top: 2px; }
  .address {
    margin-top: 16px; font-size: 14px; color: var(--text); line-height: 1.4;
  }
  .contact-list { list-style: none; margin-top: 12px; }
  .contact-list li {
    display: flex; align-items: center; gap: 8px;
    font-size: 14px; color: var(--text); line-height: 1.45;
  }
  .contact-list svg { width: 11px; height: 11px; fill: var(--brand); flex: none; }
  /* back */
  .card-back { display: flex; align-items: center; justify-content: center; }
  .card-back .brand-name { font-size: 70px; }
</style>
</head>
<body>
<main class="sheet">
  <article class="card card-front">
    <div class="portrait" role="img" aria-label="Portrait photo of the employee"></div>
    <span class="edge-tab"></span>
    <div class="details">
      <div class="brand-name">Corvale</div>
      <div class="person-name">Daniel Corwin</div>
      <div class="person-role">President</div>
      <div class="address">1780 Seabright Lane<br>Harbor Bay CA 90210</div>
      <ul class="contact-list">
        <li><svg viewBox="0 0 24 24"><path d="M6.6 10.8a15 15 0 0 0 6.6 6.6l2.2-2.2a1 1 0 0 1 1-.25 11 11 0 0 0 3.6.6 1 1 0 0 1 1 1V20a1 1 0 0 1-1 1A17 17 0 0 1 3 4a1 1 0 0 1 1-1h3.5a1 1 0 0 1 1 1c0 1.25.2 2.45.6 3.6a1 1 0 0 1-.25 1z"/></svg>555-240-0187</li>
        <li><svg viewBox="0 0 24 24"><path d="M2 5h20v14H2z M2 5l10 8 10-8" fill="none" stroke="#8fd032" stroke-width="2.5"/></svg>hello@corvale.com</li>
        <li><svg viewBox="0 0 24 24"><circle cx="12" cy="12" r="10" fill="none" stroke="#8fd032" stroke-width="2.5"/><path d="M2 12h20M12 2c3 3 3 17 0 20M12 2c-3 3-3 17 0 20" fill="none" stroke="#8fd032" stroke-width="2"/></svg>www.corvale.com</li>
      </ul>
    </div>
  </article>
  <article class="card card-back">
    <div class="brand-name">Corvale</div>
  </article>
</main>
</body>
</html>
```